Powepoint Templates From Logo

Hello,

I am looking for a template for PowerPoint presentations for a new company selling LED's. The PowerPoint should keep the look and feel of our newly designed website ( which is still under development ) http://brivoxa.com/development/

I have attached our Logo which should be included in this template.
This PowerPoint will be used towards client during demonstrations and for internal use.

This template should be complete with fonts and colors of the text for both headlines and bullets/normal text.

I guess the easiest way for me to determine what I like is to see some dummy info/text on the submitted designs.

Thanks

Industry/Entity Type

It Company

Requirements
Must have
• Should include our logo

```html
<!DOCTYPE html>
<html lang="en">
<head>
<meta charset="utf-8">
<title>Brivoxa Presentation Template</title>
<link href="https://fonts.googleapis.com/css2?family=Open+Sans:wght@400;600;700;800&family=Arvo:wght@700&display=swap" rel="stylesheet">
<style>
:root{
  --green:#8cc63f;
  --green-dark:#6fae1f;
  --grey:#6d6e71;
  --grey-light:#cfd0d2;
  --text:#5a5b5e;
  --bg:#ece8e1;
  --white:#ffffff;
}
*{box-sizing:border-box;margin:0;padding:0}
html,body{width:1200px;height:738px;overflow:hidden}
body{background:var(--bg);font-family:"Open Sans",Arial,sans-serif;color:var(--text);position:relative}
.slide{position:absolute;width:253px;height:189px;background:var(--white);box-shadow:0 2px 5px rgba(0,0,0,.18);overflow:hidden}
.footer-rule{position:absolute;left:0;right:0;top:166px;height:2px;background:var(--green)}
.footer-rule.thin{top:171px;height:1px;background:var(--green);opacity:.7}
.footer-dot{position:absolute;left:14px;top:160px;width:24px;height:24px;border-radius:50%;background:var(--green);border:3px solid var(--white)}
.footer-url{position:absolute;left:0;right:0;bottom:5px;text-align:center;font-size:6px;font-weight:700;color:var(--green)}
.heading{position:absolute;left:32px;top:14px;font-size:10.5px;font-weight:800;color:var(--green);padding-bottom:2px;border-bottom:1px solid var(--grey-light)}
.para{position:absolute;font-size:4.6px;line-height:6px;color:var(--text)}
.brand{position:absolute;display:flex;align-items:center;gap:6px}
.brand-dot{border-radius:50%;background:var(--green)}
.brand-name{font-weight:800;color:var(--green);letter-spacing:.5px}
.title{position:absolute;left:0;right:0;top:95px;text-align:center;font-size:12px;font-weight:800;color:var(--grey)}
.bullets{position:absolute;list-style:none}
.bullets li{position:relative;padding-left:10px;font-weight:700;color:var(--grey)}
.bullets li::before{content:"";position:absolute;left:0;top:50%;width:4px;height:4px;margin-top:-2px;border-radius:50%;background:var(--green)}
.band{position:absolute;left:0;right:0;top:83px;height:80px;background:linear-gradient(90deg,#8d8e90,#b9babc)}
.band-text{position:absolute;left:30px;top:22px;color:var(--white);font-size:10px;line-height:12px}
.band-text strong{font-size:12.5px;font-weight:600}
.band-photo{position:absolute;right:20px;top:10px;width:80px;height:60px;border-radius:50%;background:radial-gradient(circle,#ffffff,#d9dadb 45%,rgba(200,200,200,0) 72%)}
.part{position:absolute;left:0;right:0;top:82px;text-align:center;font-size:16px;font-weight:800;color:var(--green)}
.photo{position:absolute;left:20px;top:54px;width:102px;height:85px;background:radial-gradient(circle at 50% 45%,#cfe88f,#8cc63f 70%)}
.data-table{position:absolute;left:32px;top:42px;width:190px;border-collapse:collapse}
.data-table th{background:#7a7b7d;color:var(--white);font-size:7px;font-weight:700;height:17px}
.data-table td{font-size:4.8px;height:13px;padding-left:9px;border-bottom:1px solid #e5e5e5;border-right:1px solid #e5e5e5;color:var(--text)}
.data-table tr:nth-child(even) td{background:#f3f3f4}
.diagram{position:absolute;left:0;top:0}
.subs{position:absolute;display:flex;flex-direction:column;gap:10px}
.sub h4{position:relative;padding-left:8px;font-size:5px;font-weight:700;color:var(--grey)}
.sub h4::before{content:"";position:absolute;left:0;top:1px;width:3px;height:3px;border-radius:50%;background:var(--green)}
.sub p{font-size:4.8px;line-height:6.5px;padding-left:8px;margin-top:2px}
.thanks{position:absolute;left:0;right:0;top:108px;text-align:center;font-family:"Arvo",Georgia,serif;color:var(--green);font-weight:700}
.thanks .big{font-size:15px;display:block}
.thanks .small{font-size:7px;display:block;margin-top:2px}
</style>
</head>
<body>

<!-- Row 1 -->
<section class="slide" style="left:340px;top:41px">
  <div class="brand" style="left:78px;top:14px"><span class="brand-dot" style="width:30px;height:30px"></span><span class="brand-name" style="font-size:17px">Brivoxa</span></div>
  <div class="title">TITLE OF PRESENTATION</div>
  <div class="footer-rule"></div><div class="footer-rule thin"></div><div class="footer-dot"></div>
  <div class="footer-url">www.brivoxa.com</div>
</section>

<section class="slide" style="left:614px;top:41px">
  <h2 class="heading">LOREM IPSUM&nbsp; LOREM</h2>
  <p class="para" style="left:30px;top:46px;width:196px">Lorem ipsum dolor sit amet, consectetuer adipiscing elit, sed diam nonummy nibh euismod tincidunt ut laoreet dolore magna aliquam erat volutpat. Ut wisi enim ad minim veniam, quis nostrud exerci tation ullamcorper suscipit lobortis nisl ut aliquip ex ea commodo consequat. Duis autem vel eum iriure dolor in hendrerit in vulputate velit esse molestie consequat, vel illum dolore eu feugiat nulla facilisis.</p>
  <ul class="bullets" style="left:30px;top:96px;font-size:5.6px;line-height:11.5px">
    <li>Lorem ipsum&nbsp; Lorem Lorem ipsum&nbsp; Lorem</li>
    <li>Lorem ipsum Lorem Lorem</li>
    <li>Lorem ipsum Lorem Lorem ipsum&nbsp; Lorem&nbsp; Lorem ipsum</li>
    <li>Lorem ipsum orem Lorem ipsum&nbsp; Lo</li>
    <li>Lorem ipsum Lorem</li>
  </ul>
  <div class="footer-rule"></div><div class="footer-rule thin"></div><div class="footer-dot"></div>
  <div class="footer-url">www.brivoxa.com</div>
</section>

<section class="slide" style="left:902px;top:41px">
  <h2 class="heading" style="left:66px">LOREM IPSUM&nbsp; LOREM</h2>
  <p class="para" style="left:42px;top:40px;width:172px">Lorem ipsum dolor sit amet, consectetuer adipiscing elit, sed diam nonummy nibh euismod tincidunt ut laoreet dolore magna aliquam erat volutpat. Ut wisi enim ad minim veniam, quis nostrud exerci tation ullamcorper suscipit lobortis nisl ut aliquip ex ea commodo consequat.</p>
  <div class="band">
    <p class="band-text">Now is the time to<br><strong>switch to LED</strong></p>
    <div class="band-photo" role="img" aria-label="Glowing LED spotlight bulb"></div>
  </div>
  <div class="footer-rule"></div><div class="footer-rule thin"></div><div class="footer-dot"></div>
  <div class="footer-url">www.brivoxa.com</div>
</section>

<!-- Row 2 -->
<section class="slide" style="left:40px;top:271px">
  <div class="brand" style="left:68px;top:20px"><span class="brand-dot" style="width:34px;height:34px"></span><span class="brand-name" style="font-size:19px">Brivoxa</span></div>
  <div class="part">PART 3</div>
  <p class="para" style="left:28px;top:115px;width:198px">Lorem ipsum dolor sit amet, consectetuer adipiscing elit, sed diam nonummy nibh euismod tincidunt ut laoreet dolore magna aliquam erat volutpat. Ut wisi enim ad minim veniam, quis nostrud exerci tation ullamcorper suscipit lobortis nisl ut aliquip ex ea commodo consequat. Duis autem vel eum iriure dolor in hendrerit in vulputate velit esse molestie consequat, vel illum dolore eu feugiat nulla facilisis.</p>
  <div class="footer-rule"></div><div class="footer-rule thin"></div><div class="footer-dot"></div>
  <div class="footer-url">www.brivoxa.com</div>
</section>

<section class="slide" style="left:340px;top:271px">
  <h2 class="heading" style="left:15px">LOREM IPSUM</h2>
  <div class="photo" role="img" aria-label="LED light bulb on a green background"></div>
  <p class="para" style="left:150px;top:52px;width:92px;text-align:justify">Lorem ipsum dolor sit amet, consectetuer adipiscing elit, sed diam nonummy nibh euismod tincidunt ut laoreet dolore magna aliquam erat volutpat. Ut wisi enim ad minim veniam, quis nostrud exerci tation ullamcorper suscipit lobortis nisl ut aliquip ex ea commodo consequat. Duis autem vel eum iri. Lorem ipsum dolor sit amet, consectetuer adipiscing elit, sed diam nonummy nibh.</p>
  <div class="footer-rule"></div><div class="footer-rule thin"></div><div class="footer-dot"></div>
  <div class="footer-url">www.brivoxa.com</div>
</section>

<section class="slide" style="left:614px;top:271px">
  <h2 class="heading">LOREM IPSUM</h2>
  <table class="data-table">
    <tr><th colspan="4">Lorem ipsum&nbsp; Lorem ipsum&nbsp; Lorem ipsum</th></tr>
    <tr><td>Lorem ipsum</td><td>Lorem ipsum</td><td>Lorem ipsum</td><td>Lorem ipsum</td></tr>
    <tr><td>Lorem ipsum</td><td>Lorem ipsum</td><td>Lorem ipsum</td><td>Lorem ipsum</td></tr>
    <tr><td>Lorem ipsum</td><td>Lorem ipsum</td><td>Lorem ipsum</td><td>Lorem ipsum</td></tr>
    <tr><td>Lorem ipsum</td><td>Lorem ipsum</td><td>Lorem ipsum</td><td>Lorem ipsum</td></tr>
    <tr><td>Lorem ipsum</td><td>Lorem ipsum</td><td>Lorem ipsum</td><td>Lorem ipsum</td></tr>
    <tr><td>Lorem ipsum</td><td>Lorem ipsum</td><td>Lorem ipsum</td><td>Lorem ipsum</td></tr>
    <tr><td>Lorem ipsum</td><td>Lorem ipsum</td><td>Lorem ipsum</td><td>Lorem ipsum</td></tr>
    <tr><td>Lorem ipsum</td><td>Lorem ipsum</td><td>Lorem ipsum</td><td>Lorem ipsum</td></tr>
  </table>
  <div class="footer-rule"></div><div class="footer-rule thin"></div><div class="footer-dot"></div>
  <div class="footer-url">www.brivoxa.com</div>
</section>

<section class="slide" style="left:902px;top:271px">
  <h2 class="heading">LOREM IPSUM</h2>
  <svg class="diagram" width="253" height="189" viewBox="0 0 253 189" font-family="Open Sans, sans-serif">
    <defs>
      <g id="cyl">
        <path d="M0 4 V20 A12 4 0 0 0 24 20 V4" fill="#7a7b7d"/>
        <ellipse cx="12" cy="4" rx="12" ry="4" fill="#a7a8aa"/>
        <text x="12" y="16" font-size="4" fill="#fff" text-anchor="middle" font-weight="700">Lorem</text>
      </g>
    </defs>
    <g stroke="#b5b6b8" stroke-width=".6" fill="none">
      <path d="M36 53 V100 H48 M36 68 H40"/>
      <path d="M84 53 V125 M84 78 H78 M84 104 H78"/>
      <path d="M132 53 V125 M132 78 H126 M132 104 H126"/>
      <path d="M180 53 V125 M180 78 H174 M180 104 H174"/>
    </g>
    <g font-size="4.2" font-weight="700" fill="#fff" text-anchor="middle">
      <rect x="32" y="46" width="40" height="13" rx="1.5" fill="#8cc63f"/><text x="52" y="54">Lorem ipsum</text>
      <rect x="80" y="46" width="40" height="13" rx="1.5" fill="#8cc63f"/><text x="100" y="54">Lorem ipsum</text>
      <rect x="128" y="46" width="40" height="13" rx="1.5" fill="#8cc63f"/><text x="148" y="54">Lorem ipsum</text>
      <rect x="176" y="46" width="40" height="13" rx="1.5" fill="#8cc63f"/><text x="196" y="54">Lorem ipsum</text>
    </g>
    <use href="#cyl" x="40" y="66"/><use href="#cyl" x="40" y="95"/>
    <use href="#cyl" x="86" y="66"/><use href="#cyl" x="86" y="94"/><use href="#cyl" x="86" y="122"/>
    <use href="#cyl" x="134" y="66"/><use href="#cyl" x="134" y="94"/><use href="#cyl" x="134" y="122"/>
    <use href="#cyl" x="182" y="66"/><use href="#cyl" x="182" y="94"/><use href="#cyl" x="182" y="122"/>
  </svg>
  <div class="footer-rule"></div><div class="footer-rule thin"></div><div class="footer-dot"></div>
  <div class="footer-url">www.brivoxa.com</div>
</section>

<!-- Row 3 -->
<section class="slide" style="left:340px;top:500px">
  <h2 class="heading">LOREM IPSUM</h2>
  <ul class="bullets" style="left:22px;top:52px;font-size:5.4px;line-height:15px">
    <li>Lorem ipsum dolor sit amet, consectetuer adipiscing elit, sed diam nonummy.</li>
    <li>Lorem ipsum dolor sit amet, consectetuer adipiscing elit nummy.</li>
    <li>Lorem ipsum dolor sit amet, consectetuer adipiscing elit, sed diam nonummy.</li>
    <li>Lorem ipsum dolor sit amet, consectetuer adipiscing elit, sed diam nonummy.</li>
    <li>Lorem ipsum dolor sit amet, consectetuer adipiscing elit ummy.</li>
    <li>Lorem ipsum dolor sit amet, consectetuer.</li>
  </ul>
  <div class="footer-rule"></div><div class="footer-rule thin"></div><div class="footer-dot"></div>
  <div class="footer-url">www.brivoxa.com</div>
</section>

<section class="slide" style="left:614px;top:500px">
  <h2 class="heading">LOREM IPSUM</h2>
  <div class="subs" style="left:24px;top:48px;width:100px">
    <div class="sub"><h4>Sub Title-1</h4><p>Lorem ipsum dolor sit amet, etuer. Adipiscing elit, sed diam non tincidunt.</p></div>
    <div class="sub"><h4>Sub Title-2</h4><p>Lorem ipsum dolor sit amet, etuer. Adipiscing elit, sed diam non cidunt.</p></div>
    <div class="sub"><h4>Sub Title-3</h4><p>Lorem ipsum dolor sit amet, etuer. Edipiscing elit,onummy nibh cidunt.</p></div>
  </div>
  <div class="subs" style="left:138px;top:48px;width:110px">
    <div class="sub"><h4>Sub Title-1</h4><p>Lorem ipsum dolor sit amet, consectetuer.</p></div>
    <div class="sub"><h4>Sub Title-2</h4><p>Lorem ipsum dolor sit amet, consectetuer. Adipiscing elit, sonummy nibh cidunt.</p></div>
    <div class="sub"><h4>Sub Title-3</h4><p>Lorem ipsum dolor sit amet, consectetuer. Cdipiscing elit, s nonummy tincidunt.</p></div>
  </div>
  <div class="footer-rule"></div><div class="footer-rule thin"></div><div class="footer-dot"></div>
  <div class="footer-url">www.brivoxa.com</div>
</section>

<section class="slide" style="left:902px;top:500px">
  <div class="brand" style="left:66px;top:24px"><span class="brand-dot" style="width:36px;height:36px"></span><span class="brand-name" style="font-size:20px">Brivoxa</span></div>
  <p class="thanks"><span class="big">Thank You!</span><span class="small">For your attention</span></p>
  <div class="footer-rule"></div><div class="footer-rule thin"></div><div class="footer-dot"></div>
  <div class="footer-url">www.brivoxa.com</div>
</section>

</body>
</html>
```